Feral Horizon, a 3d voxel survival video game needs a card for gaming conventions

I am the lead developer for Feral Horizon http://www.FeralHorizon.example and need a business card to hand out at an indie gaming convention
The card would need to include the game name, website url, my name, position (Lead Developer), e-mail and phone number
The game is a 3d, voxel (with smooth terrain) based survival game with guns and wildlife. The main icon of the game would likely be a grizzly bear but I am willing to accept other designs too.
Attached is a media kit for the game with some images you can use but don't have to its just what little art I can provide. Anything on the website or from the video game can also be used. unrelated art can also be used.
Target Market(s)
Indie Developers/publishers at conferences
Industry/Entity Type
Games
Contact Information for Business Card
Name: Corwin Aldersby
Position: Lead Developer
E-mail: Pale_Lanterns@mailbox.example
Phone number: 555-207-3186

```html
<!DOCTYPE html>
<html lang="en">
<head>
<meta charset="utf-8">
<title>Feral Horizon – Business Card</title>
<link href="https://fonts.googleapis.com/css2?family=Roboto:wght@400;700&family=Saira+Semi+Condensed:wght@600&display=swap" rel="stylesheet">
<style>
  :root {
    --backdrop: #a8a5a6;
    --front-center: #dcd5b9;
    --front-edge: #3d3a22;
    --back-bg: #232427;
    --khaki: #a39a72;
    --brand-red: #9a1b1b;
    --white: #ffffff;
    --muted: #e6e6e6;
    --fur-light: #8a5a34;
    --fur-dark: #3b2416;
  }
  * { margin: 0; padding: 0; box-sizing: border-box; }
  html, body {
    width: 1200px; height: 1200px; overflow: hidden;
    background: var(--backdrop);
    font-family: "Roboto", Arial, sans-serif;
  }
  .canvas { position: relative; width: 1200px; height: 1200px; }

  .card { position: absolute; width: 714px; height: 421px; overflow: hidden; }

  .card-front {
    left: 237px; top: 118px;
    background: radial-gradient(ellipse 60% 65% at 50% 45%, var(--front-center) 0%, #b8b08c 45%, #6e6a45 80%, var(--front-edge) 100%);
  }
  .card-back { left: 229px; top: 643px; background: var(--back-bg); }

  .mascot-art {
    position: absolute;
    background: radial-gradient(ellipse at 50% 45%, var(--fur-light) 0%, #6b4328 50%, rgba(59,36,22,0) 78%);
  }
  .card-front .mascot-art { left: 228px; top: 60px; width: 160px; height: 165px; }
  .card-back .mascot-art { left: 82px; top: 90px; width: 136px; height: 135px; }

  .wordmark {
    position: absolute;
    font-family: "Roboto", Arial, sans-serif;
    font-weight: 700;
    color: var(--khaki);
    letter-spacing: 2px;
    text-transform: uppercase;
    white-space: nowrap;
    text-align: center;
  }
  .card-front .wordmark { left: 0; width: 714px; top: 238px; font-size: 44px; color: #7a3322; }
  .card-back .wordmark { left: 40px; width: 290px; top: 232px; font-size: 32px; }

  .contact { position: absolute; left: 369px; top: 118px; color: var(--white); }
  .contact-name {
    font-family: "Saira Semi Condensed", "Roboto Condensed", sans-serif;
    font-weight: 600; font-size: 27px; line-height: 34px;
  }
  .contact-role { font-size: 17px; color: var(--muted); margin-top: 0; }
  .contact-lines { list-style: none; margin-top: 30px; }
  .contact-lines li {
    display: flex; align-items: center; gap: 16px;
    font-size: 18px; line-height: 26px; color: var(--white);
  }
  .contact-lines svg { width: 20px; height: 16px; flex: none; }

  .band-khaki {
    position: absolute; left: 0; bottom: 0; width: 330px; height: 25px;
    background: var(--khaki);
  }
  .band-red { position: absolute; right: 0; bottom: 0; width: 410px; height: 54px; }
  .website {
    position: absolute; left: 369px; bottom: 16px;
    font-size: 18px; color: var(--white);
  }
</style>
</head>
<body>
<div class="canvas">

  <section class="card card-front">
    <div class="mascot-art" role="img" aria-label="Photograph of a roaring grizzly bear"></div>
    <div class="wordmark">Feral Horizon</div>
  </section>

  <section class="card card-back">
    <div class="mascot-art" role="img" aria-label="Photograph of a roaring grizzly bear"></div>
    <div class="wordmark">Feral Horizon</div>

    <div class="contact">
      <div class="contact-name">Corwin Aldersby</div>
      <div class="contact-role">Lead Developer</div>
      <ul class="contact-lines">
        <li>
          <svg viewBox="0 0 20 16" aria-hidden="true"><path fill="#fff" d="M1 5c0-2 4-3 9-3s9 1 9 3v2h-4V5H5v2H1z M4 8h12l2 7H2z"/><circle cx="10" cy="11" r="2" fill="#232427"/></svg>
          555-207-3186
        </li>
        <li>
          <svg viewBox="0 0 20 16" aria-hidden="true"><rect x="1" y="2" width="18" height="12" fill="#fff"/><path d="M1 2l9 7 9-7" fill="none" stroke="#232427" stroke-width="1.5"/></svg>
          Pale_Lanterns@mailbox.example
        </li>
      </ul>
    </div>

    <div class="band-khaki"></div>
    <svg class="band-red" viewBox="0 0 410 54" preserveAspectRatio="none" aria-hidden="true">
      <polygon points="35,0 410,0 410,54 0,54" fill="var(--brand-red)"/>
    </svg>
    <div class="website">www.feralhorizon.example</div>
  </section>

</div>
</body>
</html>
```